Build a landing page to promote a service (dialler consultation and support).

We are a call centre consultation firm and we need a landing page to promote a service. The service is Morvexa dialler consultation and support.
If you do not know what Morvexa is, please do some quick "Zumbrel" research for more information.
The landing page will be promoted with a paid advertisement, so we want something that is simple, and explains exactly what service we offer.
There are two objectives for the landing page:
1) A "call to action" which directs the user to a contact page, including a form plus all of our contact details.
2) A form for them viewers to enter their details to get a "FREE" quote for their project. This form should be placed on the main page.
Notes:
The call to action will require the viewer to enter their name, email, phone number as well as a description of their request. There will also need to be a drop down menu for the type of quote. This menu should have the following options:
1) Morvexa support
2) Morvexa hosting
3) Morvexa customisation
4) Other
We need 2 pages in total:
1) Main landing page
This is the home page. It will need to clearly indicate our services and our key selling features.
Services:
* Morvexa support
* Morvexa hosting
* Morvexa customisation
Key Selling Features:
* Australian based
* PCI complaint
* 10+ years of dialler and call centre experience
* we run a sister company which is a highly reputable 40 seat call centre, so we know first hand about call centre technology.
The main landing page will have an "about us" section with a few paragraphs about how we got started.
-------------------------------------------------------------------------
2) Contact page
All of our contact details will live on this page, as well as a contact form.
Other notes:
We will be self hosting the landing page.
We already have a domain name.
The design must be clean and incorporate our logo, as well as it's colours. (Logo attached)
We want a fully function HTML landing page, not just a "PSD" design.
The page must be mobile optimised.
Anyone using Morvexa software.

```html
<!DOCTYPE html>
<html lang="en">
<head>
<meta charset="utf-8">
<title>Tonevale – Morvexa Support, Hosting &amp; Customisation</title>
<link href="https://fonts.googleapis.com/css2?family=Lato:wght@400;700;900&display=swap" rel="stylesheet">
<style>
  :root {
    --blue: #1b7dcb;
    --teal: #22ab8f;
    --teal-dark: #1f9f86;
    --ink: #222222;
    --text: #333333;
    --white: #ffffff;
    --field-bg: #f7faf0;
    --field-line: #d9ddd2;
    --footer: #141414;
  }
  * { box-sizing: border-box; margin: 0; padding: 0; }
  html, body { width: 700px; height: 1200px; overflow: hidden; }
  body { font-family: 'Lato', sans-serif; color: var(--text); background: var(--white); position: relative; }

  /* Hero */
  .hero { position: absolute; left: 0; top: 0; width: 700px; height: 410px; }
  .hero-photo { position: absolute; inset: 0; background: linear-gradient(100deg, #c9c2b8 0%, #b7b2ab 35%, #8e8a86 60%, #3e4044 100%); }
  .hero-topline { position: absolute; left: 0; top: 0; width: 700px; height: 3px; background: var(--teal); }
  .site-header { position: absolute; left: 0; top: 3px; width: 700px; height: 73px; background: rgba(255,255,255,0.35); }
  .brand { position: absolute; left: 44px; top: 46px; display: flex; align-items: center; gap: 6px; }
  .brand-mark { width: 12px; height: 12px; border-radius: 50%; background: var(--blue); }
  .brand-name { font-size: 16px; font-weight: 700; color: var(--blue); letter-spacing: 0.3px; }
  .nav { position: absolute; top: 27px; left: 320px; display: flex; align-items: center; }
  .nav a { font-size: 11.5px; color: #2b2b2b; text-decoration: none; height: 28px; line-height: 28px; margin-right: 27px; }
  .nav a.active { background: var(--teal); color: var(--white); border-radius: 14px; padding: 0 14px; margin-right: 22px; }

  .quote-form { position: absolute; left: 414px; top: 100px; width: 212px; height: 276px; background: var(--field-bg); }
  .quote-title { height: 35px; background: var(--teal); color: var(--white); font-size: 15.5px; font-weight: 700; text-align: center; line-height: 35px; }
  .field { position: absolute; left: 13px; width: 185px; height: 27px; border: 1px solid var(--field-line); background: var(--field-bg); font-size: 8.5px; color: #666; padding: 8px 9px; }
  .field.area { height: 46px; }
  .field.select::after { content: ""; position: absolute; right: 9px; top: 10px; border-left: 4px solid transparent; border-right: 4px solid transparent; border-top: 7px solid var(--blue); }
  .submit { position: absolute; left: 458px; top: 361px; width: 124px; height: 29px; background: linear-gradient(90deg, var(--blue), var(--teal)); color: var(--white); font-size: 13px; font-weight: 700; text-align: center; line-height: 29px; }

  /* Services */
  .services { position: absolute; left: 0; top: 410px; width: 700px; height: 296px; background: linear-gradient(90deg, var(--blue), var(--teal)); }
  .notch { position: absolute; left: 330px; top: 390px; }
  .section-title { font-size: 24px; font-weight: 900; text-align: center; letter-spacing: 0.3px; }
  .services .section-title { color: var(--white); position: absolute; top: 18px; width: 100%; }
  .service-card { position: absolute; top: 72px; width: 194px; height: 191px; background: rgba(255,255,255,0.13); text-align: center; color: var(--white); }
  .service-card h3 { font-size: 13.5px; font-weight: 700; margin-top: 16px; letter-spacing: 0.2px; }
  .service-card svg { display: block; margin: 4px auto 0; }
  .service-card p { font-size: 9.6px; line-height: 14px; margin: 7px 14px 0; }
  .btn { display: inline-block; background: var(--teal); color: var(--white); font-size: 11px; border-radius: 14px; box-shadow: 0 2px 4px rgba(0,0,0,0.2); height: 28px; line-height: 28px; width: 89px; text-align: center; }
  .service-card .btn { position: absolute; left: 53px; top: 144px; }

  /* Features */
  .features { position: absolute; left: 0; top: 706px; width: 700px; height: 262px; }
  .features .section-title { position: absolute; left: 42px; top: 42px; color: var(--ink); text-align: left; }
  .feature-list { position: absolute; left: 42px; top: 86px; width: 300px; list-style: none; }
  .feature-list li { position: relative; padding-left: 22px; font-size: 9.8px; line-height: 19.5px; color: var(--ink); }
  .feature-list svg { position: absolute; left: 0; top: 5px; }
  .features .btn { position: absolute; left: 44px; top: 194px; }
  .team-photo { position: absolute; left: 358px; top: 32px; width: 299px; height: 219px; background: linear-gradient(100deg, #b9c2c6 0%, #7c858a 45%, #d8d2cc 100%); }

  /* About */
  .about { position: absolute; left: 0; top: 968px; width: 700px; height: 195px; background: linear-gradient(90deg, var(--blue), var(--teal)); color: var(--white); text-align: center; }
  .about .section-title { margin-top: 26px; }
  .about p { width: 530px; margin: 13px auto 0; font-size: 10.8px; line-height: 16px; }
  .about .btn { position: absolute; left: 306px; top: 135px; }

  .site-footer { position: absolute; left: 0; top: 1163px; width: 700px; height: 37px; background: var(--footer); color: var(--white); font-size: 8px; padding: 13px 43px; }
  .site-footer .sep { margin: 0 8px; }
</style>
</head>
<body>
  <section class="hero">
    <div class="hero-photo" role="img" aria-label="Smiling call centre agent wearing a headset at a desk, colleagues working behind him"></div>
    <div class="hero-topline"></div>
    <header class="site-header">
      <div class="brand"><span class="brand-mark"></span><span class="brand-name">Tonevale</span></div>
      <nav class="nav">
        <a class="active" href="#">Home</a>
        <a href="#">About Us</a>
        <a href="#">Services</a>
        <a href="#">Features</a>
        <a href="#">Contact Us</a>
      </nav>
    </header>
    <form class="quote-form">
      <div class="quote-title">Get a Quote “FREE”</div>
      <div class="field" style="top:53px">Name</div>
      <div class="field" style="top:90px">Email</div>
      <div class="field" style="top:129px">Phone Number</div>
      <div class="field area" style="top:167px">Description</div>
      <div class="field select" style="top:221px">Morvexa support</div>
    </form>
    <div class="submit">Submit</div>
  </section>

  <svg class="notch" width="40" height="22" viewBox="0 0 40 22" aria-hidden="true">
    <polygon points="0,22 20,2 40,22" fill="#1f8fb8"/>
    <polyline points="14,11 20,16 26,11" fill="none" stroke="#fff" stroke-width="2.2"/>
  </svg>

  <section class="services">
    <h2 class="section-title">OUR SERVICES</h2>
    <div class="service-card" style="left:43px">
      <h3>MORVEXA SUPPORT</h3>
      <svg width="54" height="54" viewBox="0 0 54 54" aria-hidden="true">
        <circle cx="27" cy="18" r="11" fill="none" stroke="#fff" stroke-width="3"/>
        <path d="M14 19a13 13 0 0 1 26 0" fill="none" stroke="#fff" stroke-width="3"/>
        <path d="M8 54v-8c0-7 8-12 19-12s19 5 19 12v8z" fill="#fff"/>
        <polygon points="27,36 24,40 27,50 30,40" fill="#2a8fc4"/>
      </svg>
      <p>Duis aute irure dolor in reprehenderit in voluptate velit esse cillum dolore eu fugiat nulla pariatur.</p>
      <span class="btn">Read more</span>
    </div>
    <div class="service-card" style="left:254px">
      <h3>MORVEXA HOSTING</h3>
      <svg width="54" height="54" viewBox="0 0 54 54" aria-hidden="true">
        <rect x="4" y="18" width="24" height="7" rx="2" fill="#fff"/>
        <rect x="4" y="27" width="24" height="7" rx="2" fill="#fff"/>
        <rect x="4" y="36" width="24" height="7" rx="2" fill="#fff"/>
        <line x1="16" y1="43" x2="16" y2="50" stroke="#fff" stroke-width="2"/>
        <line x1="6" y1="50" x2="26" y2="50" stroke="#fff" stroke-width="2"/>
        <circle cx="38" cy="14" r="7" fill="#fff"/>
        <path d="M27 34c0-8 5-12 11-12s11 4 11 12z" fill="#fff"/>
      </svg>
      <p>Duis aute irure dolor in reprehenderit in voluptate velit esse cillum dolore eu fugiat nulla pariatur.</p>
      <span class="btn">Read more</span>
    </div>
    <div class="service-card" style="left:464px">
      <h3>MORVEXA CUSTOMISATION</h3>
      <svg width="54" height="54" viewBox="0 0 54 54" aria-hidden="true">
        <circle cx="27" cy="27" r="18" fill="none" stroke="#fff" stroke-width="7" stroke-dasharray="7 5"/>
        <circle cx="27" cy="27" r="14" fill="none" stroke="#fff" stroke-width="3"/>
        <line x1="16" y1="38" x2="36" y2="18" stroke="#fff" stroke-width="5" stroke-linecap="round"/>
      </svg>
      <p>Duis aute irure dolor in reprehenderit in voluptate velit esse cillum dolore eu fugiat nulla pariatur.</p>
      <span class="btn">Read more</span>
    </div>
  </section>

  <section class="features">
    <h2 class="section-title">OUR FEATURES</h2>
    <ul class="feature-list">
      <li><svg width="11" height="9" viewBox="0 0 11 9" aria-hidden="true"><polyline points="1,4.5 4,7.5 10,1" fill="none" stroke="#22ab8f" stroke-width="2.2"/></svg>Australian based</li>
      <li><svg width="11" height="9" viewBox="0 0 11 9" aria-hidden="true"><polyline points="1,4.5 4,7.5 10,1" fill="none" stroke="#22ab8f" stroke-width="2.2"/></svg>PCI complaint</li>
      <li><svg width="11" height="9" viewBox="0 0 11 9" aria-hidden="true"><polyline points="1,4.5 4,7.5 10,1" fill="none" stroke="#22ab8f" stroke-width="2.2"/></svg>10+ years of dialler and call centre experience</li>
      <li><svg width="11" height="9" viewBox="0 0 11 9" aria-hidden="true"><polyline points="1,4.5 4,7.5 10,1" fill="none" stroke="#22ab8f" stroke-width="2.2"/></svg>we run a sister company which is a highly reputable 40 seat call centre, so we know first hand about call centre technology.</li>
    </ul>
    <span class="btn">Read more</span>
    <div class="team-photo" role="img" aria-label="Three call centre agents with headsets working at their desks"></div>
  </section>

  <section class="about">
    <h2 class="section-title">ABOUT US</h2>
    <p>Sed ut perspiciatis unde omnis iste natus error sit voluptatem accusantium doloremque laudantium, totam rem aperiam, eaque ipsa quae ab illo inventore veritatis et quasi architecto beatae vitae dicta sunt explicabo. Nemo enim ipsam voluptatem quia voluptas sit aspernatur aut odit aut fugit,</p>
    <span class="btn">Read more</span>
  </section>

  <footer class="site-footer">© 2018<span class="sep">|</span>www.companyname.com</footer>
</body>
</html>
```